Lantern Airfields Homepage Design Update

here's the current site - http://lanternairfields.example/

client is not happy with overall look.

keeping the same info - intro text, headlines, featured media excepts and general navigation options - can you come up with a nicer, slicker look for this homepage?

UPDATE: since it was asked by designer.. the general layout doesnt have to be the same. its not required to have a big image, with text below that and then smaller images/text below that. as long as we have the same content on the page, it can organized and designed in any way,

client like big images, so one way or the other, keep that... but feel free to reorganize content, explore different ways of framing it, and/or anything else. make this homepage pop!

for the designer that wins this, we'll start an additional project to update the interior.

let me know if any questions..

thanks!

marcus

Target Market(s)

aviation industry professionals, local governments, general public

Number of Pages Required

1 page

Font styles to use
Sans Serif

Requirements
Must have
• big image somewhere. same content as on current site, just designed differently.

```html
<!DOCTYPE html>
<html lang="en">
<head>
<meta charset="utf-8">
<title>Lantern Airfields</title>
<link rel="stylesheet" href="https://fonts.googleapis.com/css2?family=Josefin+Sans:wght@400;600;700&family=Lato:ital,wght@0,400;0,700;1,400&display=swap">
<style>
  :root{
    --teal:#27b8a6;
    --navy:#1f3f78;
    --blue:#2b4f9a;
    --ink:#2f3440;
    --muted:#7a7f88;
    --rule:#e2e4e8;
    --band:#f3f4f6;
    --white:#ffffff;
    --sky-top:#3f7cc0;
    --sky-mid:#8fb7e0;
    --sky-low:#e9f1f9;
    --social-a:#3b5998;
    --social-b:#d6492f;
    --social-c:#2a7fc1;
  }
  *{box-sizing:border-box;margin:0;padding:0}
  html,body{width:863px;height:1200px;overflow:hidden;background:var(--white)}
  body{font-family:"Lato",sans-serif;color:var(--ink);position:relative}
  .page{position:relative;width:863px;height:1200px;overflow:hidden}

  /* hero */
  .hero{position:absolute;left:0;top:0;width:863px;height:383px}
  .hero-photo{position:absolute;inset:0;background:linear-gradient(180deg,var(--sky-top) 0%,var(--sky-mid) 45%,var(--sky-low) 80%,#d9e3ee 100%)}
  .site-nav{position:absolute;left:0;top:0;width:863px;height:44px;display:flex;align-items:center;justify-content:space-between;padding:0 28px}
  .brand{display:flex;align-items:center;gap:7px;font-family:"Josefin Sans",sans-serif;font-weight:600;font-size:15px;color:var(--white);letter-spacing:.3px}
  .brand-dot{width:12px;height:12px;border-radius:50%;background:var(--white)}
  .menu{display:flex;gap:22px;list-style:none;font-family:"Josefin Sans",sans-serif;font-size:10px;font-weight:600;color:var(--white);letter-spacing:.6px;align-items:center}
  .menu .boxed{border:1px solid var(--white);padding:5px 8px 3px}
  .tagline{position:absolute;left:50%;transform:translateX(-50%);font-family:"Josefin Sans",sans-serif;font-weight:600;color:var(--white);text-transform:uppercase;white-space:nowrap;letter-spacing:.8px}
  .tagline-a{top:283px;background:var(--teal);font-size:17px;padding:9px 26px 6px}
  .tagline-b{top:326px;background:var(--navy);font-size:15px;padding:8px 30px 5px}
  .dots{position:absolute;top:367px;left:50%;transform:translateX(-50%);display:flex;gap:6px}
  .dots span{width:7px;height:7px;border-radius:50%;background:rgba(255,255,255,.6)}
  .dots span.on{background:var(--white)}

  /* intro */
  .intro{position:absolute;top:440px;left:0;width:863px;text-align:center}
  .intro h1{font-family:"Josefin Sans",sans-serif;font-weight:700;font-size:17px;letter-spacing:.4px;color:var(--ink)}
  .intro p{width:640px;margin:18px auto 0;font-size:10px;line-height:16px;color:var(--muted)}
  .btn{display:inline-block;background:var(--blue);color:var(--white);font-family:"Josefin Sans",sans-serif;font-weight:700;font-size:10px;letter-spacing:.6px;padding:8px 14px 6px}
  .intro .btn{margin-top:16px}

  .divider{position:absolute;left:0;top:618px;width:863px;height:1px;background:var(--rule)}

  /* featured media */
  .media-title{position:absolute;top:640px;width:863px;text-align:center;font-family:"Josefin Sans",sans-serif;font-weight:700;font-size:17px;letter-spacing:.4px}
  .arrow{position:absolute;top:708px;width:16px;height:40px}
  .arrow-left{left:36px}
  .arrow-right{left:812px}
  .cards{position:absolute;top:680px;left:80px;display:flex;gap:40px}
  .card{width:208px}
  .card-photo{height:126px;border-radius:10px;background:linear-gradient(180deg,#4d86c6 0%,#9cc1e4 60%,#c9d6e2 100%)}
  .card-photo.warm{background:linear-gradient(180deg,#3b6fb3 0%,#c98b4e 70%,#8a5a2e 100%)}
  .card-date{margin-top:58px;font-family:"Josefin Sans",sans-serif;font-weight:700;font-size:11px;color:var(--blue)}
  .card-text{margin-top:5px;font-size:9px;line-height:13px;color:var(--muted);width:170px}
  .card .btn{margin-top:10px;font-size:9px;padding:6px 10px 4px;background:var(--teal)}

  /* testimonials */
  .quotes{position:absolute;top:990px;left:0;width:863px;height:140px;background:var(--band);display:flex;justify-content:center;gap:38px;padding-top:22px}
  .quote{width:232px;display:flex;gap:8px}
  .quote-mark{font-family:"Josefin Sans",sans-serif;font-size:40px;line-height:34px;color:#b9bdc4}
  .quote p{font-style:italic;font-size:9px;line-height:13px;color:var(--muted)}
  .quote cite{display:block;margin-top:8px;font-style:normal;font-weight:700;font-size:9px;color:var(--ink)}

  /* footer */
  .site-footer{position:absolute;top:1148px;left:0;width:863px;display:flex;justify-content:space-between;align-items:center;padding:0 40px}
  .footer-links{display:flex;gap:12px;list-style:none;font-size:9px;color:var(--ink)}
  .copyright{margin-top:5px;font-size:8px;color:var(--muted)}
  .social{display:flex;gap:6px}
  .social span{width:22px;height:22px;border-radius:50%}
  .social .a{background:var(--social-a)}
  .social .b{background:var(--social-b)}
  .social .c{background:var(--social-c)}
  .social .d{background:var(--social-b)}
</style>
</head>
<body>
<div class="page">

  <header class="hero">
    <div class="hero-photo" role="img" aria-label="Passenger jet flying above white clouds in a blue sky"></div>
    <nav class="site-nav">
      <div class="brand"><span class="brand-dot"></span>Lantern Airfields</div>
      <ul class="menu">
        <li>ABOUT</li><li>SERVICES</li><li>AIRPORTS</li><li>NEWS &amp; MEDIA</li><li>CONTACT</li><li class="boxed">EMPLOYEES</li>
      </ul>
    </nav>
    <div class="tagline tagline-a">Bringing private, free enterprise business practices</div>
    <div class="tagline tagline-b">To airports throughout the U.S.</div>
    <div class="dots"><span class="on"></span><span></span><span></span><span></span></div>
  </header>

  <section class="intro">
    <h1>WE DEVELOP P3 AIRPORT OPPORTUNITIES WITHIN THE U.S. MARKET</h1>
    <p>Lantern Airfields is focused on opportunities to invest, develop and manage both general aviation and commercial service airports in key U.S. markets. A subsidiary of Lantern Holdings, a private equity firm that works in the aerospace and transportation sectors, Lantern has the resources available to invest and finance infrastructure. Lantern maintains offices in New York, Dallas and Atlanta.</p>
    <span class="btn">READ MORE</span>
  </section>

  <div class="divider"></div>

  <h2 class="media-title">FEATURED MEDIA</h2>
  <svg class="arrow arrow-left" viewBox="0 0 16 40"><polyline points="13,4 3,20 13,36" fill="none" stroke="#b9bdc4" stroke-width="2"/></svg>
  <svg class="arrow arrow-right" viewBox="0 0 16 40"><polyline points="3,4 13,20 3,36" fill="none" stroke="#b9bdc4" stroke-width="2"/></svg>

  <div class="cards">
    <article class="card">
      <div class="card-photo" role="img" aria-label="Airliner taking off against a blue sky"></div>
      <div class="card-date">January 15, 2015</div>
      <p class="card-text">Plans for Second Commercial Airport in Metro Atlanta Moving Forward</p>
      <span class="btn">READ MORE</span>
    </article>
    <article class="card">
      <div class="card-photo" role="img" aria-label="Jet aircraft in flight over clouds"></div>
      <div class="card-date">January 15, 2015</div>
      <p class="card-text">Plans for Second Commercial Airport in Metro Atlanta Moving Forward</p>
      <span class="btn">READ MORE</span>
    </article>
    <article class="card">
      <div class="card-photo warm" role="img" aria-label="Aircraft parked at an airport terminal at dusk"></div>
      <div class="card-date">January 15, 2015</div>
      <p class="card-text">Plans for Second Commercial Airport in Metro Atlanta Moving Forward</p>
      <span class="btn">READ MORE</span>
    </article>
  </div>

  <section class="quotes">
    <blockquote class="quote"><span class="quote-mark">&ldquo;</span><div><p>Praesent vestibulum aenean nonummy hendrerit mauris. Cum sociis natoque penatibus et magnis dis parturient montes nascetur ridiculus mus. Nulla dui fusce feugiat malesuada odio morbi nunc odio gravida.</p><cite>Dana Reyes, Manager</cite></div></blockquote>
    <blockquote class="quote"><span class="quote-mark">&ldquo;</span><div><p>Praesent vestibulum aenean nonummy hendrerit mauris. Cum sociis natoque penatibus et magnis dis parturient montes nascetur ridiculus mus. Nulla dui fusce feugiat malesuada odio morbi nunc odio gravida.</p><cite>Dana Reyes, Manager</cite></div></blockquote>
    <blockquote class="quote"><span class="quote-mark">&ldquo;</span><div><p>Praesent vestibulum aenean nonummy hendrerit mauris. Cum sociis natoque penatibus et magnis dis parturient montes nascetur ridiculus mus. Nulla dui fusce feugiat malesuada odio morbi nunc odio gravida.</p><cite>Dana Reyes, Manager</cite></div></blockquote>
  </section>

  <footer class="site-footer">
    <div>
      <ul class="footer-links"><li>Home</li><li>About</li><li>Services</li><li>Airports</li><li>News &amp; Media</li><li>Contact</li><li>Employees</li><li>Terms of Use</li></ul>
      <div class="copyright">© 2015 Lantern Airfields. All rights reserved.</div>
    </div>
    <div class="social"><span class="a"></span><span class="b"></span><span class="c"></span><span class="d"></span></div>
  </footer>

</div>
</body>
</html>
```